Burly Mates Yard Ad creatives contest

I neednew ad banner for my site I can use to advertise on other adult sites our site is for Tradies and blue color workers to build their adult brands of themselves with videos streaming and market place and chat we have allt he things. I want to incorporate masculine men who are normal gay not all muscle thing like hairy dad bods who don't go to the gym every day t are still fit and healthly and not at over weight. It's for the normal guys who are working men. Im open to funny xxx, and a mix of nude and full on sex scenes. My clients maotly ahve a sense of humor and anything that's unique or makes people laugh or their brain want to click.. click bate all the way. This is for only men who like men so no hetero or females please. Here is some of the stuff we have had previously. Remember it's technically a porn site so please use nudes mainly I'm I dont. Have pictures to supply sorry. But think lumberjack masculine dad's body working men. Muscle is ok but not like Adonis model think what your bf looks like or if your a dude prolly your body.
Target Market(s)
Gay, bisexual and straight men who like blue- collar men and porn.
Industry/Entity Type
Adult entertainment
Requirements
Must have
- Partial nudity if not.full nude.. website logo and "burly mates yard" somewhere

Nice to have
- Nudes of masculine men, and half naked regular adverage men ok n

Should not have
- Women or heterosexual references

```html
<!DOCTYPE html>
<html lang="en">
<head>
<meta charset="utf-8">
<title>Burly Mates Yard – Ad Banners</title>
<link href="https://fonts.googleapis.com/css2?family=Barlow+Semi+Condensed:wght@700&family=Barlow+Condensed:wght@700&family=Exo+2:wght@400;500&display=swap" rel="stylesheet">
<style>
  :root{
    --page:#ffffff;
    --ink-dark:#1c1c1c;
    --sun:#fbb91f;
    --tangerine:#e97d42;
    --button-orange:#f4874b;
    --lime:#6ef04a;
    --brown:#3b2611;
    --white:#ffffff;
    --black:#141414;
  }
  *{margin:0;padding:0;box-sizing:border-box}
  html,body{width:1158px;height:1200px;overflow:hidden;background:var(--page)}
  .canvas{position:relative;width:1158px;height:1200px}
  .banner{position:absolute;left:52px;width:1052px;height:526px;overflow:hidden}
  .banner--grit{top:39px;background:var(--ink-dark)}
  .banner--bedroom{top:612px;left:54px;background:var(--tangerine)}
  .banner svg.backdrop{position:absolute;inset:0}
  .photo{position:absolute}
  .brand{position:absolute;left:90px;top:25px;display:flex;align-items:center;gap:12px;z-index:2}
  .brand__dot{width:58px;height:58px;border-radius:50%;background:var(--brown)}
  .brand__name{font-family:"Exo 2",sans-serif;font-weight:500;font-size:17px;color:var(--white)}
  .headline{position:absolute;font-weight:700;text-transform:uppercase;white-space:nowrap;z-index:2}
  .banner--grit .headline{font-family:"Barlow Semi Condensed","Arial Narrow",sans-serif;left:90px;top:135px;font-size:56px;line-height:66px;letter-spacing:.3px}
  .t-orange{color:var(--tangerine)} .t-lime{color:var(--lime)} .t-white{color:var(--white)} .t-black{color:var(--black)}
  .copy{position:absolute;font-family:"Exo 2",sans-serif;font-size:15px;line-height:22.5px;color:var(--white);z-index:2}
  .banner--grit .copy{left:90px;top:280px;width:360px}
  .cta{position:absolute;width:143px;height:45px;border-radius:5px;font-family:"Exo 2",sans-serif;font-size:15px;color:var(--white);display:flex;align-items:center;justify-content:center;z-index:2}
  .banner--grit .cta{left:91px;top:370px;background:var(--button-orange)}
  .banner--bedroom .headline{font-family:"Barlow Condensed","Arial Narrow",sans-serif;left:80px;top:152px;font-size:74px;line-height:76px;letter-spacing:1px}
  .banner--bedroom .copy{left:82px;top:235px;width:410px}
  .banner--bedroom .cta{left:82px;top:324px;background:var(--brown)}
</style>
</head>
<body>
<div class="canvas">

  <section class="banner banner--grit">
    <svg class="backdrop" width="1052" height="526" viewBox="0 0 1052 526">
      <polygon points="430,0 1052,0 1052,526 860,526 720,390 650,280 620,110" fill="var(--sun)"/>
    </svg>
    <div class="photo" role="img" aria-label="Photo of a shirtless man with arms raised behind his head" style="left:665px;top:80px;width:375px;height:446px;border-radius:190px 190px 0 0;background:radial-gradient(ellipse at 50% 40%,#a8705a,#6a3f2e 60%,#3b2611)"></div>
    <div class="brand"><span class="brand__dot"></span><span class="brand__name">Burly Mates Yard</span></div>
    <h1 class="headline"><span class="t-orange">Workin</span> <span class="t-lime">Hard ? Or</span><br><span class="t-lime">Hardly</span> <span class="t-white">Working</span></h1>
    <p class="copy">Lorem ipsum dolor sit amet, consectetur adipiscing elit, sed do eiusmod tempor incididunt ut labore et dolore magna aliqua.</p>
    <div class="cta">Request Quote</div>
  </section>

  <section class="banner banner--bedroom">
    <div class="photo" role="img" aria-label="Photo of a shirtless man in white briefs reclining on a bed in a bright bedroom" style="left:420px;top:0;width:632px;height:526px;background:linear-gradient(90deg,var(--tangerine) 0%,rgba(233,125,66,0) 28%),linear-gradient(180deg,#6b5a4c 0%,#9c8f84 40%,#c9b3a0 70%,#d8d4cf 100%)"></div>
    <div class="brand"><span class="brand__dot"></span><span class="brand__name">Burly Mates Yard</span></div>
    <h1 class="headline"><span class="t-black">Burly Mates</span> <span class="t-white">Yard</span></h1>
    <p class="copy">Lorem ipsum dolor sit amet, consectetur adipiscing elit, sed do eiusmod tempor incididunt ut labore et dolore magna aliqua.</p>
    <div class="cta">Request Quote</div>
  </section>

</div>
</body>
</html>
```